Healthy Supplement featuring Moringa products

Need 3 business card options for our reps to order from Cardloom. Our reps will be ordering from Cardloom once we upload them. Attached is our current designs to show what info needs to be on the cards. Our website is www.tkvitality.com
The business cards will be a template for our reps to order from. Most of our reps are Asian & Hispanic. Please look at our website so you can see who we are to get the look and feel what we need.
Target Market(s)
Adults 30 on up. Health oriented people.
Industry/Entity Type
Health And Wellness
Contact Information for Business Card
Name
Title
Phone
Logo
www.tkvitality.com/my/username
Font styles to use
Requirements
Must have
- Please match our website look and colors. A moringa leaf is nice, but am open to something different.
Nice to have
- Healthy looking and warm, not super cold or too modern.
Should not have
- No harsh colors please.

```html
<!DOCTYPE html>
<html lang="en">
<head>
<meta charset="utf-8">
<title>TK Vitality Business Card</title>
<link href="https://fonts.googleapis.com/css2?family=Open+Sans:wght@400;600;700&display=swap" rel="stylesheet">
<style>
  :root {
    --backdrop: #9b9b9b;
    --card: #ffffff;
    --leaf-green: #6aa512;
    --light-green: #8cc61a;
    --warm-orange: #f7941d;
    --ink: #555555;
  }
  * { margin: 0; padding: 0; box-sizing: border-box; }
  html, body {
    width: 1133px; height: 1200px; overflow: hidden;
    background: var(--backdrop);
    font-family: "Open Sans", sans-serif;
  }
  .card {
    position: absolute;
    left: 218px;
    width: 697px; height: 398px;
    background: var(--card);
  }
  .card--front { top: 153px; }
  .card--back { top: 646px; }

  .brand {
    position: absolute;
    display: flex; align-items: center; gap: 10px;
    color: var(--leaf-green);
    font-weight: 700;
    white-space: nowrap;
  }
  .brand__dot {
    border-radius: 50%;
    background: var(--light-green);
    flex: none;
  }
  .card--front .brand {
    right: 50px; top: 72px;
    font-size: 34px;
  }
  .card--front .brand__dot { width: 34px; height: 34px; }

  .holder { position: absolute; left: 46px; top: 222px; }
  .holder__name {
    color: var(--leaf-green);
    font-weight: 700; font-size: 24px; line-height: 1.1;
  }
  .holder__title {
    color: var(--warm-orange);
    font-size: 17px; line-height: 1.3;
  }
  .contact {
    position: absolute; left: 46px; top: 290px;
    list-style: none;
  }
  .contact__item {
    display: flex; align-items: center;
    height: 23px;
    color: var(--ink); font-size: 17px;
  }
  .contact__icon {
    width: 18px; height: 18px; margin-right: 12px; flex: none;
    fill: var(--leaf-green);
  }

  .card--back .brand {
    left: 0; right: 0; top: 150px;
    justify-content: center;
    font-size: 58px; gap: 16px;
  }
  .card--back .brand__dot { width: 56px; height: 56px; }
  .back__web {
    position: absolute; left: 0; right: 0; top: 338px;
    text-align: center;
    color: var(--ink);
    font-size: 18px; letter-spacing: 6px;
  }
</style>
</head>
<body>
  <section class="card card--front">
    <div class="brand"><span class="brand__dot"></span>TK Vitality</div>
    <div class="holder">
      <div class="holder__name">Marco Reyes</div>
      <div class="holder__title">President</div>
    </div>
    <ul class="contact">
      <li class="contact__item">
        <svg class="contact__icon" viewBox="0 0 20 20" aria-hidden="true"><path d="M2 7c0-3 3-4 8-4s8 1 8 4v2h-4V7H6v2H2z"/><path d="M5 10h10l2 7H3z"/><circle cx="10" cy="13.5" r="2" fill="#fff"/></svg>
        (555) 0142-7781
      </li>
      <li class="contact__item">
        <svg class="contact__icon" viewBox="0 0 20 20" aria-hidden="true"><path d="M1 5h18v11H1z"/><path d="M1 5l9 6 9-6" fill="none" stroke="#fff" stroke-width="1.6"/></svg>
        info@tkvitality.com
      </li>
      <li class="contact__item">
        <svg class="contact__icon" viewBox="0 0 20 20" aria-hidden="true"><circle cx="10" cy="10" r="9"/><path d="M6 6c2 0 3 1 3 3s-2 2-2 4l1 3c-3-1-5-4-4-7zM12 4c2 1 3 3 3 5-1 0-2-1-3-1s-1-2 0-4z" fill="#fff"/></svg>
        www.tkvitality.com
      </li>
    </ul>
  </section>

  <section class="card card--back">
    <div class="brand"><span class="brand__dot"></span>TK Vitality</div>
    <div class="back__web">www.tkvitality.com</div>
  </section>
</body>
</html>
```